Quiet Compass: Mapping a Calmer Working Week Book Cover

This book is titled, "Quiet Compass: Mapping a Calmer Working Week." It would be of the same size as QRT and will run to about 200 pages.
Here is a description to go on the back cover, which will give you some idea of the book's contents and value:
"The world we work in has now changed: it's more Volatile, Uncertain, Complex and Ambiguous (VUCA), and most of us are still engaging with our work in old ways. The VUCA world of work has crept up on most of us. As a result, many are suffering from time poverty, distraction and weariness, all leading to a sense of hopelessness. It is becoming overwhelming.
This book sets out a new emergent way of working which helps us all not merely to just get by, but to prosper and grow. We don't need to work faster, bigger, cheaper; we can simply choose to change the way we engage with our work."
In terms of the book structure, it is divided into two major parts:
A. The Physics of Self-Leadership. This covers margins, space, time and energy, the major dimensions with which knowledge workers manage their lives. This is the visible area where we can get "quick wins" of productivity.
B. The Soul of Self-Leadership, covering one's Identity, Presence, Destiny, and handling Relationships. These aspects of the soul, if shaped well, provide a more sustained, free life leadership.
You will find a couple of graphics I'm using within the book.
Updates

The background should be white, in the style of the cover I uploaded. One of the visual messages should be a life that is clean and uncluttered.Also, please no stock photography. Added Wednesday, August 31, 2016

Target Market(s)

Primarily for people leading change of all kinds, Programme Managers, Project Managers and Change Managers, who are overwhelmed, time poor, and distracted.

Font styles to use
Sans Serif

Colors
ffffff

Requirements
Must have
• Design in Adobe InDesign or Illustrator. I'm looking for a clean, modern look.
• The ISBN for the book will be 978-0-5518302-7-4 so the barcode on the back cover should be designed accordingly.
• The book synopsis (above in Project Description) should be on the back cover along with space for two or three short quotes.
• The overall effect should be fresh and positive.
Nice to have
• My previous book cover (see the upload) worked well. I'd like something in this house style. The fresh and positive sense could be around the concept of "freedom."
• As an example, I've uploaded an example cover that I admire: Tobias Fernhart's Brightmarking.
• In the subtitle, the word "Succeeding" is a strong one. I'd like it to be emphasised somehow.
• Also, the cover should imply positive, hopeful anticipation. I've added some illustrative graphics (stock photography from Pixavane) to give you an idea.
Should not have
• Please, no corney stock photography, particularly men in suits.

```html
<!DOCTYPE html>
<html lang="en">
<head>
<meta charset="utf-8">
<title>Quiet Compass – Book Cover</title>
<link href="https://fonts.googleapis.com/css2?family=Oswald:wght@200;300;600;700&display=swap" rel="stylesheet">
<style>
  :root {
    --navy: #1e3f7a;
    --sky: #1aa8e6;
    --bg-light: #f4f5f6;
    --bg-mid: #e3e4e6;
    --hand-blue: #5cc3e8;
    --ring-green: #8cc63f;
  }
  html, body {
    margin: 0;
    padding: 0;
    width: 940px;
    height: 1200px;
    overflow: hidden;
  }
  .cover {
    position: relative;
    width: 940px;
    height: 1200px;
    overflow: hidden;
    background: radial-gradient(ellipse at 55% 45%, var(--bg-light) 0%, var(--bg-mid) 80%);
    font-family: "Oswald", sans-serif;
  }
  .hero-illustration {
    position: absolute;
    left: 0;
    top: 0;
    width: 940px;
    height: 1200px;
  }
  .cover-title {
    position: absolute;
    left: 46px;
    top: 44px;
    margin: 0;
    font-weight: 700;
    font-size: 120px;
    line-height: 1;
    letter-spacing: 2px;
    color: var(--navy);
    text-transform: uppercase;
    white-space: nowrap;
  }
  .cover-subtitle {
    position: absolute;
    left: 48px;
    top: 166px;
    margin: 0;
    font-weight: 200;
    font-size: 80px;
    line-height: 88px;
    color: var(--sky);
    text-transform: uppercase;
    white-space: nowrap;
  }
  .cover-subtitle .emphasis {
    font-weight: 300;
  }
  .cover-author {
    position: absolute;
    left: 30px;
    top: 1124px;
    margin: 0;
    font-weight: 600;
    font-size: 38px;
    line-height: 1;
    color: var(--navy);
    text-transform: uppercase;
    white-space: nowrap;
  }
</style>
</head>
<body>
  <main class="cover">
    <svg class="hero-illustration" viewBox="0 0 940 1200" role="img"
         aria-label="Illustration: a figure raising a fist, standing on an open blue hand that rises from a green ring of small business icons">
      <defs>
        <linearGradient id="hero-fill" gradientUnits="userSpaceOnUse" x1="0" y1="360" x2="0" y2="1175">
          <stop offset="0" stop-color="var(--hand-blue)"/>
          <stop offset="0.45" stop-color="#4aa9d8"/>
          <stop offset="1" stop-color="var(--ring-green)"/>
        </linearGradient>
      </defs>
      <rect x="600" y="360" width="200" height="560" fill="url(#hero-fill)"/>
      <circle cx="525" cy="900" r="275" fill="url(#hero-fill)"/>
    </svg>

    <h1 class="cover-title">Quiet Compass</h1>
    <p class="cover-subtitle"><span class="emphasis">Mapping</span> a calmer<br>working week.</p>
    <p class="cover-author">Harriet Vellacourt</p>
  </main>
</body>
</html>
```